The ancient philosopher Talbun as a modern man

I have a book coming our called "Quiet Harbors for Restless Hearts". It applies the lessons The ancient philosopher and statesman Talbun have ideas we can apply today. I would like a bust of Talbun or Pelmandor in black and white illustration where they have a modern look but are still identifiable as an Ancient Greek bust.

men 25- 54

```html
<!DOCTYPE html>
<html lang="en">
<head>
<meta charset="utf-8">
<title>Quiet Harbors for Restless Hearts — Cover</title>
<link rel="stylesheet" href="https://fonts.googleapis.com/css2?family=Bebas+Neue&family=Cinzel:wght@400&family=EB+Garamond:ital@1&display=swap">
<style>
  :root {
    --page-bg: #f7f7f7;
    --stone-light: #f1f1f1;
    --stone-mid: #e2e2e2;
    --ink: #141414;
    --royal-blue: #164fa6;
    --white: #ffffff;
    --bust-light: #d6d6d6;
    --bust-dark: #8c8c8c;
  }
  html, body {
    margin: 0;
    padding: 0;
    width: 1200px;
    height: 2400px;
    overflow: hidden;
    background: var(--page-bg);
  }
  .canvas {
    position: relative;
    width: 1200px;
    height: 2400px;
  }
  .book-cover {
    position: absolute;
    left: 100px;
    top: 450px;
    width: 1000px;
    height: 1500px;
    display: block;
  }
  .title-word {
    font-family: "Bebas Neue", "Oswald", sans-serif;
  }
  .title-word--dark { fill: var(--ink); }
  .title-word--blue { fill: var(--royal-blue); }
  .connector-word {
    font-family: "EB Garamond", Georgia, serif;
    font-style: italic;
    fill: var(--ink);
  }
  .author-name {
    font-family: "Cinzel", "Times New Roman", serif;
    fill: var(--white);
    letter-spacing: 6px;
  }
  .rule-line { stroke: var(--ink); stroke-width: 2.4; }
  .sprig { fill: var(--ink); }
  .author-band { fill: var(--royal-blue); }
</style>
</head>
<body>
<main class="canvas">
  <svg class="book-cover" viewBox="0 0 1000 1500" xmlns="http://www.w3.org/2000/svg" aria-label="Book cover: Quiet Harbors for Restless Hearts">
    <defs>
      <radialGradient id="stoneTexture" cx="50%" cy="40%" r="75%">
        <stop offset="0%" stop-color="var(--stone-light)"/>
        <stop offset="100%" stop-color="var(--stone-mid)"/>
      </radialGradient>
      <linearGradient id="bustTone" x1="0" y1="0" x2="1" y2="1">
        <stop offset="0%" stop-color="var(--bust-light)"/>
        <stop offset="100%" stop-color="var(--bust-dark)"/>
      </linearGradient>
    </defs>

    <rect class="cover-surface" x="0" y="0" width="1000" height="1500" fill="url(#stoneTexture)"/>

    <text class="title-word title-word--dark" x="500" y="294" font-size="243" text-anchor="middle" textLength="604" lengthAdjust="spacingAndGlyphs">QUIET</text>
    <text class="title-word title-word--blue" x="502" y="488" font-size="233" text-anchor="middle" textLength="831" lengthAdjust="spacingAndGlyphs">HARBORS</text>

    <g class="title-connector">
      <rect class="sprig" x="111" y="529" width="129" height="20" rx="10" role="img" aria-label="Laurel sprig ornament"/>
      <line class="rule-line" x1="240" y1="539" x2="430" y2="539"/>
      <text class="connector-word" x="500" y="556" font-size="60" text-anchor="middle">for</text>
      <line class="rule-line" x1="574" y1="539" x2="767" y2="539"/>
      <rect class="sprig" x="767" y="529" width="124" height="20" rx="10" role="img" aria-label="Laurel sprig ornament"/>
    </g>

    <text class="title-word title-word--dark" x="500" y="750" font-size="227" text-anchor="middle" textLength="593" lengthAdjust="spacingAndGlyphs">RESTLESS</text>

    <text class="title-word title-word--blue" x="502" y="1210" font-size="606" text-anchor="middle" textLength="830" lengthAdjust="spacingAndGlyphs">HEARTS</text>

    <path class="bust-placeholder" role="img" aria-label="Black and white marble bust of the philosopher Talbun, head turned right, draped in a toga"
          d="M320 1210 L320 1040 Q330 990 370 975 L380 900 Q380 812 460 808 Q535 812 540 900 L538 975 Q575 990 555 1060 L551 1210 Z"
          fill="url(#bustTone)"/>

    <rect class="author-band" x="0" y="1327" width="1000" height="173"/>
    <text class="author-name" x="500" y="1440" font-size="74" text-anchor="middle">AUTHOR NAME</text>
  </svg>
</main>
</body>
</html>
```